BRAVEN VOLTWORKS SERVICES needs a vibrant design for electrical contracting work.

I require a card design for my own electrical contracting business. I will be doing a lot of domestic and commercial work, including things such as repairs, maintenance, lighting, installations and various others. LED lighting and energy efficiency will be a big part of my business. I wish not to have childish pictures such as light bulbs in the design, but rather a smart and modern looking card which incorporates my logo colours and perhaps the same lighting strike within the faded background of the card.

Target Market(s)

Residential and Commercial property owners.

Industry/Entity Type

Electrical

Contact Information for Business Card

Dario Pesek
EC40362
Phone Number: 0417 538 924
Email: dario@bravenvoltworks.com

Font styles to use
Serif
Sans Serif

Requirements
Must have
• My Logo and associated colours.
Nice to have
• Some form of shapes splitting the card into different colours related to the colours of my logo. Electric Blue, Silver/Grey and White.
Should not have
• Childish pictures and symbols such as light bulbs.

```html
<!DOCTYPE html>
<html lang="en">
<head>
<meta charset="utf-8">
<title>Braven Voltworks Services – Business Card</title>
<link rel="stylesheet" href="https://fonts.googleapis.com/css2?family=Lato:wght@400;700;900&display=swap">
<style>
  :root {
    --page-bg: #e6e7ea;
    --card-white: #ffffff;
    --electric-blue: #3651a8;
    --silver-light: #d9dadc;
    --silver-mid: #9a9b9e;
    --silver-dark: #6f7073;
    --text-white: #ffffff;
    --logo-grey: #8c8d90;
  }
  * { margin: 0; padding: 0; box-sizing: border-box; }
  html, body {
    width: 1200px;
    height: 900px;
    overflow: hidden;
    background: var(--page-bg);
    font-family: "Lato", Arial, sans-serif;
  }
  .business-card {
    position: absolute;
    left: 100px;
    top: 164px;
    width: 1000px;
    height: 572px;
    background: var(--card-white);
    box-shadow: 0 10px 30px rgba(0, 0, 0, 0.18);
    overflow: hidden;
  }
  .card-shapes {
    position: absolute;
    inset: 0;
    width: 100%;
    height: 100%;
  }
  .brand-lockup {
    position: absolute;
    left: 60px;
    top: 108px;
    display: flex;
    align-items: center;
    gap: 16px;
  }
  .brand-mark {
    width: 44px;
    height: 44px;
    border-radius: 50%;
    background: var(--logo-grey);
  }
  .brand-name {
    font-weight: 900;
    font-size: 28px;
    letter-spacing: 1px;
    color: var(--electric-blue);
    line-height: 1;
  }
  .licence-number {
    position: absolute;
    right: 50px;
    top: 108px;
    font-weight: 700;
    font-size: 28px;
    letter-spacing: 0.5px;
    color: var(--text-white);
  }
  .contact-block {
    position: absolute;
    right: 42px;
    top: 372px;
    text-align: right;
    color: var(--text-white);
  }
  .contact-name {
    font-weight: 400;
    font-size: 38px;
    letter-spacing: 1.5px;
    margin-bottom: 22px;
    margin-right: 8px;
  }
  .contact-line {
    display: flex;
    justify-content: flex-end;
    align-items: center;
    gap: 14px;
    font-size: 26px;
    letter-spacing: 0.5px;
    margin-bottom: 14px;
  }
  .contact-icon {
    width: 24px;
    height: 24px;
    fill: var(--text-white);
  }
</style>
</head>
<body>
  <div class="business-card">
    <svg class="card-shapes" viewBox="0 0 1000 572" preserveAspectRatio="none" aria-hidden="true">
      <defs>
        <linearGradient id="silverPanel" x1="0" y1="0" x2="1" y2="1">
          <stop offset="0" stop-color="var(--silver-mid)"/>
          <stop offset="0.45" stop-color="var(--silver-light)"/>
          <stop offset="1" stop-color="var(--silver-dark)"/>
        </linearGradient>
      </defs>
      <polygon class="silver-panel" points="630,0 1000,0 1000,232 565,319" fill="url(#silverPanel)"/>
      <polygon class="blue-band" points="0,440 1000,240 1000,572 0,572" fill="var(--electric-blue)"/>
      <line class="band-divider" x1="565" y1="328" x2="1000" y2="241" stroke="var(--card-white)" stroke-width="5"/>
    </svg>

    <div class="brand-lockup">
      <div class="brand-mark"></div>
      <div class="brand-name">BRAVEN VOLTWORKS SERVICES</div>
    </div>

    <div class="licence-number">EC40362</div>

    <div class="contact-block">
      <div class="contact-name">DARIO PESEK</div>
      <div class="contact-line">
        <span>0417 538 924</span>
        <svg class="contact-icon" viewBox="0 0 24 24" aria-hidden="true">
          <path d="M6.6 10.8c1.4 2.8 3.8 5.1 6.6 6.6l2.2-2.2c.3-.3.7-.4 1-.2 1.1.4 2.3.6 3.6.6.6 0 1 .4 1 1V20c0 .6-.4 1-1 1C10.6 21 3 13.4 3 4c0-.6.4-1 1-1h3.5c.6 0 1 .4 1 1 0 1.3.2 2.5.6 3.6.1.3 0 .7-.2 1l-2.3 2.2z"/>
        </svg>
      </div>
      <div class="contact-line">
        <span>dario@bravenvoltworks.com</span>
        <svg class="contact-icon" viewBox="0 0 24 24" aria-hidden="true">
          <path d="M2 5h20v14H2z M2 5l10 8 10-8" fill="var(--text-white)"/>
          <path d="M2 5l10 8 10-8" fill="none" stroke="var(--electric-blue)" stroke-width="1.6"/>
        </svg>
      </div>
    </div>
  </div>
</body>
</html>
```